need to update our new address on letterhead and business cards. Also open to
a redesign and logo in the near future as we are changing our name. New address is Bramcote Commerce Court, 781 Ashgrove Street, Linwood Hollow, CT 06287

Target Market(s)

35-75 yrs of age

Industry/Entity Type

Business

Requirements
Nice to have
• We are a financial firm so this need to look impressive and classy

```html
<!DOCTYPE html>
<html lang="en">
<head>
<meta charset="utf-8">
<title>Halvorsen Financial Letterhead</title>
<link rel="stylesheet" href="https://fonts.googleapis.com/css2?family=Cormorant+Garamond:wght@500&family=Roboto:wght@400&display=swap">
<style>
  :root {
    --backdrop: #e8d7aa;
    --paper: #ffffff;
    --navy: #1c2f5e;
    --accent-blue: #2e5c93;
    --accent-grey: #c9ccd2;
    --icon-tone: #b9ad8a;
    --rule: #dcd8cc;
  }
  * { margin: 0; padding: 0; box-sizing: border-box; }
  html, body {
    width: 1200px; height: 784px; overflow: hidden;
    background: var(--backdrop);
  }
  .letterhead {
    position: absolute; left: 322px; top: 28px;
    width: 556px; height: 728px;
    background: var(--paper);
    box-shadow: 0 2px 10px rgba(120, 95, 40, 0.18);
  }
  .corner-bar {
    position: absolute; width: 6px;
    background: linear-gradient(to bottom, var(--accent-blue) 70%, var(--accent-grey));
  }
  .corner-bar--left { left: 0; top: 0; height: 64px; }
  .corner-bar--right { right: 0; top: 18px; height: 52px; }
  .brand-block {
    position: absolute; right: 22px; top: 16px;
    text-align: right; color: var(--navy);
  }
  .brand-name {
    font-family: "Cormorant Garamond", Georgia, serif;
    font-weight: 500; font-size: 27px; line-height: 1.1;
    margin-bottom: 6px;
  }
  .contact-line {
    font-family: "Cormorant Garamond", Georgia, serif;
    font-weight: 500; font-size: 10.5px; line-height: 14px;
    display: flex; justify-content: flex-end; align-items: center; gap: 5px;
    white-space: nowrap;
  }
  .contact-icon {
    width: 7px; height: 7px; border-radius: 50%;
    background: var(--icon-tone); display: inline-block; flex: none;
  }
  .contact-spacer { width: 7px; display: inline-block; flex: none; }
  .footer-rule {
    position: absolute; left: 56px; right: 40px; bottom: 52px;
    height: 1px; background: var(--rule);
  }
  .disclaimer {
    position: absolute; left: 16px; right: 16px; bottom: 24px;
    font-family: "Roboto", Arial, sans-serif; font-weight: 400;
    font-size: 6.5px; line-height: 10px;
    color: var(--navy); text-align: center;
  }
  .disclaimer-line { display: block; white-space: nowrap; }
  .bottom-bar {
    position: absolute; left: 0; bottom: 0;
    width: 72%; height: 6px;
    background: linear-gradient(to right, var(--accent-blue) 85%, var(--accent-grey));
  }
</style>
</head>
<body>
  <main class="letterhead">
    <div class="corner-bar corner-bar--left"></div>
    <div class="corner-bar corner-bar--right"></div>

    <header class="brand-block">
      <div class="brand-name">Halvorsen Financial</div>
      <div class="contact-line">Bramcote Commerce Court <span class="contact-spacer"></span></div>
      <div class="contact-line">781 Ashgrove Street, Linwood Hollow, CT 06287 <span class="contact-icon"></span></div>
      <div class="contact-line">555-210-0148 <span class="contact-icon"></span> 555-210-0162 <span class="contact-icon"></span></div>
      <div class="contact-line">RLangford@HalvorsenFinancialSvcs.com <span class="contact-icon"></span></div>
      <div class="contact-line">www.HalvorsenFinancialSvcs.com <span class="contact-icon"></span></div>
    </header>

    <div class="footer-rule"></div>
    <footer class="disclaimer">
      <span class="disclaimer-line">Securities offered through Alderwick Financial Specialists LLC, member NSRA/SPIF. Advisory services offered through Alderwick Investment Advisers LLC.</span>
      <span class="disclaimer-line">Alderwick entities are under separate ownership from any other entity.</span>
    </footer>
    <div class="bottom-bar"></div>
  </main>
</body>
</html>
```